Luxury startup skincare company needs packaging design

We want a label design for glass jars and a packaging box. The label design will be unique, clean, classy, and expensive looking. The design must be eye-catching and colorful, bold and universal. I

I've attached the logo variations for your reference. The glass jar will need a label for the top as well as a wrap-around label and the packaging will need to be designed per specs that will be provided. We currently have one product and will be expanding to several once the brand grows.

Target Market(s)

Women with disposable income 25-65 years old who care about their skincare routine

Industry/Entity Type

Beauty

Font styles to use
Decorative

Requirements
Must have
• my logo

```html
<!DOCTYPE html>
<html lang="en">
<head>
<meta charset="UTF-8">
<title>Umber Crest – Repairing Mask Label</title>
<link rel="stylesheet" href="https://fonts.googleapis.com/css2?family=Libre+Baskerville:wght@700&family=Montserrat:wght@700&family=Raleway:wght@400;500&family=Roboto+Condensed:wght@400&display=swap">
<style>
  :root {
    --canvas: #ffffff;
    --label-black: #141213;
    --rose: #d8a198;
    --rose-light: #e9b9b0;
    --rose-deep: #b57a72;
    --ink-white: #f4f2f1;
    --ink-soft: #dcd8d6;
    --ink-dark: #2a1f1d;
  }
  * { margin: 0; padding: 0; box-sizing: border-box; }
  html, body {
    width: 1200px;
    height: 1030px;
    overflow: hidden;
    background: var(--canvas);
  }
  .label {
    position: absolute;
    left: 0;
    top: 235px;
    width: 1200px;
    height: 560px;
    background: var(--label-black);
    overflow: hidden;
  }
  .info-column {
    position: absolute;
    font-family: "Roboto Condensed", sans-serif;
    font-size: 12.5px;
    line-height: 1.55;
    color: var(--ink-white);
  }
  .info-column p + p { margin-top: 16px; }
  .info-column--left {
    left: 40px;
    top: 50px;
    width: 250px;
  }
  .info-column--right {
    left: 880px;
    top: 60px;
    width: 230px;
    text-align: right;
  }
  .brand {
    position: absolute;
    left: 335px;
    top: 135px;
    width: 355px;
    display: flex;
    align-items: center;
    gap: 14px;
    white-space: nowrap;
  }
  .brand__dot {
    flex: none;
    width: 22px;
    height: 22px;
    border-radius: 50%;
    background: var(--rose);
  }
  .brand__name {
    font-family: "Raleway", sans-serif;
    font-weight: 400;
    font-size: 26px;
    letter-spacing: 6px;
    color: var(--ink-white);
  }
  .product-title {
    position: absolute;
    left: 305px;
    top: 250px;
    width: 380px;
    text-align: center;
    font-family: "Libre Baskerville", serif;
    font-weight: 700;
    font-size: 52px;
    line-height: 1.12;
    color: var(--ink-white);
    white-space: nowrap;
  }
  .feature-band {
    position: absolute;
    left: 318px;
    top: 412px;
    width: 330px;
    height: 42px;
    background: var(--rose);
    border-radius: 0 21px 21px 0;
    font-family: "Montserrat", sans-serif;
    font-weight: 700;
    font-size: 17px;
    color: var(--ink-dark);
    display: flex;
    align-items: center;
    justify-content: center;
    letter-spacing: 0.3px;
  }
  .tagline {
    position: absolute;
    left: 330px;
    top: 470px;
    width: 320px;
    text-align: center;
    font-family: "Raleway", sans-serif;
    font-weight: 500;
    font-size: 17px;
    line-height: 1.3;
    color: var(--ink-soft);
  }
  .profile-art {
    position: absolute;
    left: 720px;
    top: -10px;
    width: 120px;
    height: 580px;
    border-radius: 70px 10px 60px 20px;
    background: linear-gradient(180deg, var(--rose-light) 0%, var(--rose) 55%, var(--rose-deep) 100%);
  }
  .spec-box {
    position: absolute;
    left: 1040px;
    top: 400px;
    width: 100px;
    height: 96px;
    background: var(--canvas);
  }
</style>
</head>
<body>
  <section class="label">
    <div class="info-column info-column--left">
      <p>Our rich repairing mask wraps each strand in argan oil and shea butter, sealing in moisture and softening dry ends. Smooth a generous amount through clean damp hair, leave for ten minutes, then rinse well.</p>
      <p>Made for curls, coils and waves that crave deep care. Gentle plant oils restore shine and bounce while helping reduce breakage from heat, styling and daily wear. Free from sulfates, parabens and mineral oil.</p>
      <p>For external use only. Avoid contact with eyes; if contact occurs, rinse at once with water. Stop use if irritation appears. Store in a cool, dry place away from direct sunlight and close the lid after use.</p>
    </div>

    <div class="brand">
      <span class="brand__dot"></span>
      <span class="brand__name">UMBER CREST</span>
    </div>

    <h1 class="product-title">REPAIRING<br>MASK</h1>
    <div class="feature-band">INFUSED WITH ARGAN OIL</div>
    <p class="tagline">Deep moisturization to replenish and help restore hair health</p>

    <div class="profile-art" role="img" aria-label="Rose-gold side-profile silhouette of a woman with flowing hair"></div>

    <div class="info-column info-column--right">
      <p>Argan oil is pressed from the kernels of the argan tree and is rich in vitamin E and fatty acids that nourish the hair shaft.</p>
      <p>Weekly use leaves hair softer, stronger and easier to detangle, with a lasting glow and a light floral scent.</p>
    </div>

    <div class="spec-box"></div>
  </section>
</body>
</html>
```